Business Card for beauty technology startup

Design Glowmi Business Card for a Beauty, based on the website identity and colors (https://www.glowmi-example.com).
Glowmi is a beauty tech startup that gathers helpful product info for beauty lovers and consumers (such as availability on stores, price range and product reviews) for makeup products. The card design must be young, colorful but clean, and very modern.

Target Market(s)

woman, 15-35

Industry/Entity Type

Cosmetics

Contact Information for Business Card

Full Name, address, phone

Font styles to use
Other font styles liked:
• Advent Pro

Colors
e34297
86cfc6
ffffff
5c5c5c
e8e8e8
e667a6
b2b2b2

Requirements
Must have
• One full colored side with a creative design and another with card info
• Use Color palette: #95C5C5 and/or #D38AA5
• Use fonts: Advent Pro
• Use website identity: https://www.glowmi-example.com
Nice to have
• If needed extra font: Roboto

```html
<!DOCTYPE html>
<html lang="en">
<head>
<meta charset="utf-8">
<title>Glowmi Business Card</title>
<link href="https://fonts.googleapis.com/css2?family=Advent+Pro:wght@300;400;500&display=swap" rel="stylesheet">
<style>
  :root {
    --pink: #e34297;
    --pink-soft: #e667a6;
    --pink-pale: #f09ac4;
    --white: #ffffff;
    --grey-text: #5c5c5c;
    --backdrop: #a3a3a3;
  }
  * { margin: 0; padding: 0; box-sizing: border-box; }
  html, body { width: 1200px; height: 982px; overflow: hidden; }
  body {
    background: var(--backdrop);
    font-family: "Advent Pro", sans-serif;
    position: relative;
  }
  .card {
    position: absolute;
    top: 176px;
    width: 360px;
    height: 630px;
    overflow: hidden;
    background: var(--pink);
  }
  .card-front { left: 200px; }
  .card-back { left: 640px; background: var(--white); }
  .card-shapes { position: absolute; inset: 0; }

  .brand {
    position: absolute;
    left: 0; right: 0;
    top: 215px;
    display: flex;
    flex-direction: column;
    align-items: center;
    color: var(--white);
  }
  .brand-circle {
    width: 84px; height: 84px;
    border: 3px solid var(--white);
    border-radius: 50%;
  }
  .brand-name {
    margin-top: 22px;
    font-size: 46px;
    font-weight: 300;
    letter-spacing: 10px;
    text-transform: uppercase;
  }
  .front-url {
    position: absolute;
    right: 40px;
    bottom: 38px;
    font-size: 20px;
    color: var(--grey-text);
  }

  .person {
    position: absolute;
    right: 28px;
    top: 30px;
    text-align: right;
  }
  .person-name {
    font-size: 42px;
    font-weight: 400;
    color: var(--pink);
    line-height: 1;
  }
  .person-title {
    font-size: 18px;
    color: var(--grey-text);
    margin-top: 2px;
  }
  .back-brand {
    position: absolute;
    left: 0; right: 0;
    top: 335px;
    display: flex;
    align-items: center;
    justify-content: center;
    gap: 12px;
    color: var(--white);
  }
  .back-brand-circle {
    width: 44px; height: 44px;
    border: 3px solid var(--white);
    border-radius: 50%;
  }
  .back-brand-name {
    font-size: 30px;
    font-weight: 400;
    letter-spacing: 3px;
  }
  .contact-list {
    position: absolute;
    left: 78px;
    top: 440px;
    list-style: none;
    color: var(--white);
    font-size: 21px;
  }
  .contact-item {
    display: flex;
    align-items: center;
    gap: 16px;
    height: 44px;
  }
  .contact-icon { width: 20px; height: 20px; flex: none; }
</style>
</head>
<body>

<section class="card card-front">
  <svg class="card-shapes" viewBox="0 0 360 630" aria-hidden="true">
    <polygon points="0,0 360,0 0,165" fill="var(--pink-soft)" opacity="0.7"/>
    <polygon points="0,0 360,0 360,12 0,110" fill="var(--pink-pale)" opacity="0.35"/>
    <polygon points="0,455 360,482 360,630 0,630" fill="var(--pink-soft)"/>
    <polygon points="222,476 360,484 360,630 0,630 0,612" fill="var(--white)"/>
  </svg>
  <div class="brand">
    <span class="brand-circle"></span>
    <span class="brand-name">Glowmi</span>
  </div>
  <p class="front-url">www.glowmi-example.com</p>
</section>

<section class="card card-back">
  <svg class="card-shapes" viewBox="0 0 360 630" aria-hidden="true">
    <polygon points="0,50 360,285 360,630 0,630" fill="var(--pink-pale)"/>
    <polygon points="0,105 360,300 360,630 0,630" fill="var(--pink-soft)" opacity="0.85"/>
    <polygon points="0,170 360,345 360,630 0,630" fill="var(--pink)"/>
  </svg>
  <div class="person">
    <p class="person-name">Mara Lind</p>
    <p class="person-title">Managing director</p>
  </div>
  <div class="back-brand">
    <span class="back-brand-circle"></span>
    <span class="back-brand-name">Glowmi</span>
  </div>
  <ul class="contact-list">
    <li class="contact-item">
      <svg class="contact-icon" viewBox="0 0 24 24" aria-hidden="true"><path fill="#fff" d="M6.6 10.8a15 15 0 0 0 6.6 6.6l2.2-2.2a1 1 0 0 1 1-.25 11.4 11.4 0 0 0 3.6.57 1 1 0 0 1 1 1V20a1 1 0 0 1-1 1A17 17 0 0 1 3 4a1 1 0 0 1 1-1h3.5a1 1 0 0 1 1 1c0 1.25.2 2.45.57 3.57a1 1 0 0 1-.25 1z"/></svg>
      <span>555-010-0199</span>
    </li>
    <li class="contact-item">
      <svg class="contact-icon" viewBox="0 0 24 24" aria-hidden="true"><rect x="2" y="5" width="20" height="14" fill="#fff"/><polyline points="2,5 12,13 22,5" fill="none" stroke="var(--pink)" stroke-width="1.8"/></svg>
      <span>name@glowmi-example.com</span>
    </li>
    <li class="contact-item">
      <svg class="contact-icon" viewBox="0 0 24 24" aria-hidden="true"><g fill="none" stroke="#fff" stroke-width="2"><circle cx="12" cy="12" r="9"/><ellipse cx="12" cy="12" rx="4" ry="9"/><line x1="3" y1="12" x2="21" y2="12"/></g></svg>
      <span>www.glowmi-example.com</span>
    </li>
  </ul>
</section>

</body>
</html>
```